Book Cover

Book cover for a study guide on Galatians. The title would be: "Unbound Hearts: Called Out to Walk Open" Possibly using a bird breaking free from a cage.+

Target Market(s)

We will sell them to our church.

Requirements
Must have
• Authors are Dr. Martin Oskerby and Dr. Helen Oskerby

```html
<!DOCTYPE html>
<html lang="en">
<head>
<meta charset="utf-8">
<title>Unbound Hearts: Called Out to Walk Open — Book Cover</title>
<link href="https://fonts.googleapis.com/css2?family=Archivo:wght@500;600;700&family=Courier+Prime:wght@700&display=swap" rel="stylesheet">
<style>
  :root {
    --page-bg: #f4f4f4;
    --sky: #c4d7ee;
    --wash: #e6dfb8;
    --slate: #55657a;
    --gold: #dca434;
    --gold-light: #efc35a;
    --gold-dark: #c78d22;
    --navy: #1e3558;
    --paper: #fbfbf8;
    --rust: #b5662a;
  }
  * { box-sizing: border-box; margin: 0; padding: 0; }
  html, body {
    width: 1200px;
    height: 1200px;
    overflow: hidden;
    background: var(--page-bg);
  }
  .book-cover {
    position: absolute;
    left: 270px;
    top: 50px;
    width: 660px;
    height: 1100px;
    overflow: hidden;
    background: var(--sky);
  }
  .cover-art {
    position: absolute;
    inset: 0;
    background:
      radial-gradient(ellipse 55% 22% at 78% 10%, rgba(230,223,184,0.95), rgba(230,223,184,0) 70%),
      radial-gradient(ellipse 60% 30% at 55% 62%, rgba(230,223,184,0.7), rgba(230,223,184,0) 70%),
      radial-gradient(ellipse 40% 20% at 70% 45%, rgba(85,101,122,0.45), rgba(85,101,122,0) 70%),
      radial-gradient(ellipse 50% 22% at 65% 85%, rgba(85,101,122,0.55), rgba(85,101,122,0) 70%),
      radial-gradient(ellipse 30% 18% at 5% 55%, rgba(85,101,122,0.4), rgba(85,101,122,0) 70%),
      linear-gradient(180deg, var(--sky) 0%, #cbdcee 50%, var(--sky) 100%);
  }
  .cross-vertical {
    position: absolute;
    left: 73px;
    top: 0;
    width: 152px;
    height: 946px;
    background: linear-gradient(100deg, var(--gold-dark), var(--gold) 35%, var(--gold-light) 60%, var(--gold) 100%);
  }
  .cross-horizontal {
    position: absolute;
    left: 0;
    top: 154px;
    width: 297px;
    height: 165px;
    background: linear-gradient(100deg, var(--gold-dark), var(--gold) 40%, var(--gold-light) 70%, var(--gold) 100%);
  }
  .title-vertical {
    position: absolute;
    left: 73px;
    top: 34px;
    width: 152px;
    font-family: "Archivo", sans-serif;
    font-weight: 600;
    font-size: 56px;
    line-height: 62px;
    color: var(--navy);
    text-align: center;
    display: flex;
    flex-direction: column;
    align-items: center;
  }
  .title-vertical .gap { height: 24px; }
  .title-panel {
    position: absolute;
    left: 297px;
    top: 250px;
    width: 363px;
    height: 150px;
    background: var(--paper);
    padding: 42px 24px 0 22px;
    text-align: right;
  }
  .subtitle {
    font-family: "Archivo", sans-serif;
    font-weight: 600;
    font-size: 27px;
    color: var(--navy);
    white-space: nowrap;
    text-align: left;
  }
  .authors {
    margin-top: 22px;
    font-family: "Courier Prime", monospace;
    font-weight: 700;
    font-size: 14px;
    line-height: 17px;
    color: var(--rust);
  }
</style>
</head>
<body>
  <main class="book-cover">
    <div class="cover-art" role="img" aria-label="Watercolour wash of pale sky blue and gold with a flock of grey pigeons flying upward"></div>
    <div class="cross-vertical"></div>
    <div class="cross-horizontal"></div>
    <h1 class="title-vertical" aria-label="Unbound Hearts">
      <span>U</span><span>N</span><span>B</span><span>O</span><span>U</span><span>N</span><span>D</span>
      <span class="gap"></span>
      <span>H</span><span>E</span><span>A</span><span>R</span><span>T</span><span>S</span>
    </h1>
    <section class="title-panel">
      <h2 class="subtitle">Called Out to Walk Open</h2>
      <p class="authors">Dr. Martin Oskerby<br>Dr. Helen Oskerby</p>
    </section>
  </main>
</body>
</html>
```